Torvane Travel Business Card Design

We need a new business card design for our travel agency business - Torvane Travel. We design packages to some of the most popular travel destinations in the world for groups, individuals and also tailor-make personalised packages. Our logo attached must be used. On the back of the card we would like a list of all websites under our Torvane brand to be posted. We would like clean, modern, simple design.

Industry/Entity Type

Travel Agent

Contact Information for Business Card

Owen Pridmore
National Sales Manager
Reservations: 1300 742 689
Tel: 61 28473 5096
Fax: 61 2847 3971
Email: owen@torvanetravel.com.au
Web: www.torvanetravel.com.au

Address: Level 1, 417 Harwick Street
Sydney NSW 2000 Australia

Requirements
Must have
• On the back of the card we want all websites listed under our Torvane brand.
• Torvane Travel Group - Wholesale Specialists
• www.qpjourneys.com.au - New Caledonia
• www.bravelmijourneys.com.au - Tahiti
• www.sorvenbreakhub.com.au - China
Nice to have
• Modern, clean lined, simple and fresh
Should not have
• Look dull

```html
<!DOCTYPE html>
<html lang="en">
<head>
<meta charset="utf-8">
<title>Torvane Travel – Business Card</title>
<link href="https://fonts.googleapis.com/css2?family=Lato:wght@400;700;900&display=swap" rel="stylesheet">
<style>
  :root {
    --navy: #2e2f7f;
    --red: #e31e24;
    --white: #ffffff;
    --ink: #2e2f7f;
    --backdrop: #e9e7e3;
  }
  * { margin: 0; padding: 0; box-sizing: border-box; }
  html, body {
    width: 1200px; height: 800px; overflow: hidden;
    background: var(--backdrop);
    font-family: "Lato", Arial, sans-serif;
  }
  .canvas {
    width: 1200px; height: 800px;
    display: flex; align-items: center; justify-content: center; gap: 40px;
  }
  .card {
    position: relative;
    width: 540px; height: 308px;
    box-shadow: 0 6px 18px rgba(0,0,0,0.18);
    overflow: hidden;
  }

  /* Front */
  .card-front { background: var(--white); }
  .brand-block {
    position: absolute; left: 0; top: 0; width: 250px; height: 290px;
    display: flex; align-items: center; justify-content: center;
  }
  .brand-name {
    font-weight: 900; font-size: 34px; color: var(--navy);
    letter-spacing: -0.5px; white-space: nowrap;
  }
  .divider {
    position: absolute; left: 262px; top: 40px; width: 2px; height: 212px;
    background: var(--navy);
  }
  .divider::before {
    content: ""; position: absolute; left: 0; top: 0; width: 2px; height: 40px;
    background: var(--red);
  }
  .details {
    position: absolute; left: 282px; top: 40px; width: 245px;
    color: var(--ink); font-size: 11.5px; line-height: 1.45;
  }
  .person-name { color: var(--red); font-weight: 900; font-size: 19px; line-height: 1.15; }
  .person-role { margin-bottom: 16px; }
  .contact-list { list-style: none; margin-bottom: 16px; }
  .contact-list li { display: flex; align-items: center; gap: 7px; }
  .contact-list svg { width: 11px; height: 11px; flex: none; fill: var(--red); }
  .address { }
  .band {
    position: absolute; left: 0; bottom: 0; width: 100%; height: 18px;
  }

  /* Back */
  .card-back {
    background: var(--navy); color: var(--white);
    display: flex; flex-direction: column; align-items: center; justify-content: center;
    text-align: center;
  }
  .card-back .brand-name { color: var(--white); font-size: 40px; margin-bottom: 34px; }
  .site-list { list-style: none; font-size: 14px; line-height: 1.5; }
</style>
</head>
<body>
<main class="canvas">

  <section class="card card-front" aria-label="Business card front">
    <div class="brand-block">
      <span class="brand-name">Torvane Travel</span>
    </div>
    <div class="divider"></div>
    <div class="details">
      <p class="person-name">Owen Pridmore</p>
      <p class="person-role">National Sales Manager<br>Reservations: 1300 742 689</p>
      <ul class="contact-list">
        <li><svg viewBox="0 0 24 24" aria-hidden="true"><path d="M6.6 10.8a15.5 15.5 0 0 0 6.6 6.6l2.2-2.2c.3-.3.7-.4 1-.2 1.1.4 2.3.6 3.6.6.6 0 1 .4 1 1V20c0 .6-.4 1-1 1C10.6 21 3 13.4 3 4c0-.6.4-1 1-1h3.5c.6 0 1 .4 1 1 0 1.3.2 2.5.6 3.6.1.3 0 .7-.2 1z"/></svg>61 28473 5096</li>
        <li><svg viewBox="0 0 24 24" aria-hidden="true"><path d="M7 3h8v5H7zM4 9h16a1 1 0 0 1 1 1v10a1 1 0 0 1-1 1H4a1 1 0 0 1-1-1V10a1 1 0 0 1 1-1zm3 4v2h10v-2z"/></svg>61 2847 3971</li>
        <li><svg viewBox="0 0 24 24" aria-hidden="true"><path d="M2 5h20v14H2zm2 2v.5l8 5 8-5V7l-8 5z"/></svg>owen@torvanetravel.com.au</li>
        <li><svg viewBox="0 0 24 24" aria-hidden="true"><path d="M12 2a10 10 0 1 0 0 20 10 10 0 0 0 0-20zm6.9 6h-3a15 15 0 0 0-1.3-3.9A8 8 0 0 1 18.9 8zM12 4c.8 1.2 1.5 2.5 1.9 4h-3.8c.4-1.5 1.1-2.8 1.9-4zM4.3 14a8 8 0 0 1 0-4h3.4a16 16 0 0 0 0 4zm.8 2h3a15 15 0 0 0 1.3 3.9A8 8 0 0 1 5.1 16zm3-8h-3a8 8 0 0 1 4.3-3.9A15 15 0 0 0 8.1 8zM12 20c-.8-1.2-1.5-2.5-1.9-4h3.8c-.4 1.5-1.1 2.8-1.9 4zm2.3-6H9.7a14 14 0 0 1 0-4h4.6a14 14 0 0 1 0 4zm.3 5.9a15 15 0 0 0 1.3-3.9h3a8 8 0 0 1-4.3 3.9zm1.7-5.9a16 16 0 0 0 0-4h3.4a8 8 0 0 1 0 4z"/></svg>www.torvanetravel.com.au</li>
      </ul>
      <p class="address">Level 1, 417 Harwick Street<br>Sydney NSW 2000 Australia</p>
    </div>
    <svg class="band" viewBox="0 0 540 18" preserveAspectRatio="none" aria-hidden="true">
      <polygon points="0,6 380,6 372,18 0,18" fill="var(--red)"/>
      <polygon points="386,0 540,0 540,18 374,18" fill="var(--navy)"/>
    </svg>
  </section>

  <section class="card card-back" aria-label="Business card back">
    <span class="brand-name">Torvane Travel</span>
    <ul class="site-list">
      <li>Torvane Travel Group - Wholesale Specialists</li>
      <li>www.qpjourneys.com.au - New Caledonia</li>
      <li>www.bravelmijourneys.com.au - Tahiti</li>
      <li>www.sorvenbreakhub.com.au - China</li>
    </ul>
  </section>

</main>
</body>
</html>
```